Corporate-Design für LOM  Agroarbeiten
Corporate-Design für LOM Agroarbeiten
julialenzberger suchte ein neues Design in der Kategorie Corporate Design und hat ein Projekt auf entwurfsplatz.de gestartet.
Zielgruppe
Schneeräumung, Baggerarbeiten, Landwirtschaftsarbeiten
Aufgabenstellung
LOM sollte im Logo verwendet werden und auch gut lesbar sein.
Bitte auch den Landwirtschaftsbereich nicht ganz weglassen und wenn nur die grüne Farbe integriert ist. Logo sollte auch auf einen Bagger oder Traktor passen und ist nicht für einen noblen Eingangsbereich etc. gedacht.

```html
<!DOCTYPE html>
<html lang="de">
<head>
<meta charset="utf-8">
<title>LOM Agroarbeiten – Corporate Design</title>
<link href="https://fonts.googleapis.com/css2?family=Michroma&family=Arimo:wght@400;700&display=swap" rel="stylesheet">
<style>
  :root {
    --green: #6ac230;
    --dark: #4d4a47;
    --ink: #222;
    --faint: #d6d6d3;
    --faint-green: #cfe6bf;
    --paper: #ffffff;
    --wide: "Michroma", sans-serif;
    --body: "Arimo", Arial, sans-serif;
  }
  * { margin: 0; padding: 0; box-sizing: border-box; }
  html, body { width: 1200px; height: 1200px; overflow: hidden; background: #fff; }
  .board { position: relative; width: 1200px; height: 1200px; font-family: var(--body); color: var(--ink); }
  .abs { position: absolute; }

  /* brand name block */
  .brand { position: absolute; display: flex; flex-direction: column; align-items: center; }
  .brand-row { display: flex; align-items: center; }
  .brand-name { font-family: var(--wide); color: var(--dark); line-height: 1; letter-spacing: 0.02em; white-space: nowrap; }
  .brand-dot { background: var(--green); flex: none; }
  .brand-sub { font-family: var(--wide); color: var(--dark); white-space: nowrap; letter-spacing: 0.01em; }

  /* letterhead */
  .letterhead { left: 17px; top: 14px; width: 648px; height: 916px; background: var(--paper);
    box-shadow: 6px 6px 18px rgba(0,0,0,.35); }
  .tab-dark, .tab-green { position: absolute; left: 0; }
  .tab-dark { background: var(--dark); }
  .tab-green { background: var(--green); }
  .letter-text { position: absolute; font-size: 8.5px; line-height: 10px; white-space: nowrap; }
  .letter-body { font-size: 9.5px; }
  .watermark .brand-name { color: var(--faint); }
  .watermark .brand-dot { background: var(--faint-green); }
  .footer-col { position: absolute; top: 848px; height: 68px; border-left: 3px solid var(--dark);
    padding-left: 10px; font-size: 8px; line-height: 10.5px; padding-top: 3px; white-space: nowrap; }

  /* business card */
  .card { left: 556px; top: 318px; width: 490px; height: 316px; background: var(--paper);
    box-shadow: 4px 6px 16px rgba(0,0,0,.35); }
  .card-name { position: absolute; top: 186px; width: 100%; text-align: center; font-weight: 700;
    font-size: 30px; letter-spacing: 0.03em; color: #111; }
  .card-contact { position: absolute; top: 253px; font-size: 12.5px; line-height: 15px; white-space: nowrap; }
  .card-contact b { font-weight: 700; }

  /* colour panels */
  .panel-green { left: 0; top: 947px; width: 598px; height: 253px; background: var(--green); }
  .panel-dark { left: 600px; top: 947px; width: 600px; height: 253px; background: var(--dark); }
  .on-colour .brand-name, .on-colour .brand-sub { color: #fff; }

  .contact-lines { font-family: var(--wide); color: var(--dark); letter-spacing: 0.35em; white-space: nowrap; line-height: 1.15; }
  .contact-lines .phone { color: var(--green); }
</style>
</head>
<body>
<main class="board">

  <!-- Letterhead -->
  <section class="abs letterhead">
    <div class="brand" style="left:268px; top:42px; width:120px;">
      <div class="brand-row">
        <span class="brand-name" style="font-size:28px;">LOM</span>
        <span class="brand-dot" style="width:8px;height:8px;margin-left:5px;"></span>
      </div>
      <span class="brand-sub" style="font-size:5.8px;margin-top:6px;">LENZBERGER AGRO SERVICE</span>
    </div>

    <div class="tab-dark" style="top:125px;width:32px;height:16px;"></div>
    <div class="tab-green" style="top:141px;width:32px;height:16px;"></div>

    <p class="letter-text" style="left:93px;top:124px;">Beat Lenzberger • Mühlackerstrasse • Wila</p>
    <p class="letter-text" style="left:93px;top:139px;">Max Mustermann<br>Straße<br>Ort<br>MWST Nr. CHE-123456789 MWST</p>
    <p class="letter-text letter-body" style="left:93px;top:290px;">Sehr geehrter Herr,</p>
    <p class="letter-text letter-body" style="left:93px;top:346px;">Mit freundlichen Grüßen</p>
    <p class="letter-text letter-body" style="left:93px;top:372px;line-height:12px;">Name<br>Beat Lenzberger</p>

    <div class="brand watermark" style="left:211px;top:432px;width:229px;">
      <div class="brand-row">
        <span class="brand-name" style="font-size:62px;">LOM</span>
        <span class="brand-dot" style="width:16px;height:16px;margin-left:10px;"></span>
      </div>
    </div>

    <div class="footer-col" style="left:80px;">Beat Lenzberger<br>Mühlackerstrasse<br>8492 Wila</div>
    <div class="footer-col" style="left:269px;">Tel.: +41 (0) 765432<br>E-mail: info@lom-agro.ch</div>
    <div class="footer-col" style="left:470px;">Bankverbindung: xxxxxxxxxx<br>IBAN: xxxxxxxxxxxxxx<br>BIC: xxxxxxxxxxxxxxxxx</div>
  </section>

  <!-- Large logo -->
  <div class="brand" style="left:777px;top:112px;width:342px;">
    <div class="brand-row">
      <span class="brand-name" style="font-size:92px;">LOM</span>
      <span class="brand-dot" style="width:22px;height:22px;margin-left:14px;"></span>
    </div>
    <span class="brand-sub" style="font-size:15.5px;margin-top:22px;">LENZBERGER AGRO SERVICE</span>
  </div>

  <!-- Business card -->
  <section class="abs card">
    <div class="tab-dark" style="top:57px;width:37px;height:18px;"></div>
    <div class="tab-green" style="top:75px;width:37px;height:18px;"></div>
    <div class="brand" style="left:131px;top:52px;width:234px;">
      <div class="brand-row">
        <span class="brand-name" style="font-size:58px;">LOM</span>
        <span class="brand-dot" style="width:14px;height:14px;margin-left:9px;"></span>
      </div>
      <span class="brand-sub" style="font-size:10.5px;margin-top:14px;">LENZBERGER AGRO SERVICE</span>
    </div>
    <h1 class="card-name">BEAT LENZBERGER</h1>
    <p class="card-contact" style="left:37px;">Mühlackerstrasse<br>8492 Wila</p>
    <p class="card-contact" style="left:184px;text-align:right;width:120px;"><b>tel.</b> 01234 765432<br><b>mobile.</b> 01234 765</p>
    <p class="card-contact" style="left:316px;text-align:right;width:155px;"><b>email.</b> post@lom-agro.ch<br><b>website.</b> www.lom-agro.ch</p>
  </section>

  <!-- Logo with contact lines -->
  <div class="brand" style="left:780px;top:690px;width:345px;">
    <div class="brand-row">
      <span class="brand-name" style="font-size:92px;">LOM</span>
      <span class="brand-dot" style="width:22px;height:22px;margin-left:14px;"></span>
    </div>
    <span class="brand-sub" style="font-size:15.5px;margin-top:22px;">LENZBERGER AGRO SERVICE</span>
    <div class="contact-lines" style="font-size:19px;margin-top:2px;text-align:center;">
      8492 WILA<br><span class="phone">TEL.: +41 7654321</span>
    </div>
  </div>

  <!-- Colour panels -->
  <section class="abs panel-green on-colour">
    <div class="brand" style="left:145px;top:62px;width:278px;">
      <div class="brand-row">
        <span class="brand-name" style="font-size:76px;">LOM</span>
        <span class="brand-dot" style="width:19px;height:19px;margin-left:12px;background:#fff;"></span>
      </div>
      <span class="brand-sub" style="font-size:12.8px;margin-top:22px;">LENZBERGER AGRO SERVICE</span>
    </div>
  </section>
  <section class="abs panel-dark on-colour">
    <div class="brand" style="left:165px;top:52px;width:278px;">
      <div class="brand-row">
        <span class="brand-name" style="font-size:76px;">LOM</span>
        <span class="brand-dot" style="width:19px;height:19px;margin-left:12px;"></span>
      </div>
      <span class="brand-sub" style="font-size:12.8px;margin-top:22px;">LENZBERGER AGRO SERVICE</span>
    </div>
  </section>

</main>
</body>
</html>
```